Real Estate 24"x24" Sign, Business Card, Letter Head and Envelope

This is a 4 project contest. If we choose a design or designs we like from what you sent we are willing to pay an amount at our discretion for that design even if we don't like all your designs for the 4 projects. Please be creative. Attached are our logo files. Please message us with any questions. Thanks and Good Luck!
Project 1: QLTV Realty 24" x 24" yard sign
We want to use the same blue background in our logo for the sign where the logo in white font will be on. CMYK 100,80,0,0. Attached is a sample a local designer made for you to get an idea what we are looking for. In the sample, the website is way too big and the entire sign is very plain and not attractive looking plus blue color is wrong one. We want the logo on top as large as possible but keeping it proportionate and attractive looking buy not too big that it looks odd. The following information can go in white color background or same blue color background color. Our company colors are blue (as per logo), green (as per logo), and white. "Residential & Commercial" goes under the logo. Under that put our phone number "312-948-6051" as large as possible but still looks good and under that our website in much smaller but readable font "www.qltvrealty.com".
Project 2: Envelope
We have two version of the logo. Use one or both. Whatever looks best in your design. The envelope will be white. We only want on top left corner logo and underneath our mailing address: 5197 Larchmere Ave. Skokie, IL 60093-1725. Maybe some creative decorative design at bottom of envelope will look nice
Project 3: Letter Head
We have two version of the logo. Use one or both. Whatever looks best in your design. We want the following information on the top of the letterhead. Logo, address: 5197 Larchmere Ave., Skokie, IL 60093-1725, phone: 312-948-6051, fax: 312-682-9307 website www.qltvrealty.com, email: info@qltvrealty.com
Project 4: Business card
Use either logo. We need cards for two individuals. Information for Person 1: Dev Kulkarni, Managing Broker, Phone: 312-948-6051, Email: dev.kulkarni@qltvrealty.com. Person 2: Ajay Kulkarni Broker Phone: 312-519-8263 Email: ajay.kulkarni@qltvrealty.com. Add Address, Fax and website same as above letter head.

```html
<!DOCTYPE html>
<html lang="en">
<head>
<meta charset="utf-8">
<title>QLTV Realty Business Card</title>
<link href="https://fonts.googleapis.com/css2?family=Montserrat:wght@400;500;600;700&display=swap" rel="stylesheet">
<style>
  :root {
    --brand-blue: #1f62b4;
    --brand-green: #6cc24a;
    --card-white: #f4f4f2;
    --page-bg: #e9ebe8;
    --text-white: #ffffff;
  }
  * { box-sizing: border-box; margin: 0; padding: 0; }
  html, body {
    width: 1200px;
    height: 801px;
    overflow: hidden;
    background: var(--page-bg);
    font-family: "Montserrat", Arial, sans-serif;
  }
  .canvas {
    position: relative;
    width: 1200px;
    height: 801px;
    display: flex;
    align-items: center;
    justify-content: center;
    gap: 60px;
  }
  .card {
    position: relative;
    width: 520px;
    height: 297px;
    box-shadow: 0 6px 18px rgba(0, 0, 0, 0.12);
  }
  .card-front {
    background: var(--card-white);
    display: flex;
    align-items: center;
    justify-content: center;
  }
  .brand-lockup {
    display: flex;
    align-items: center;
    gap: 12px;
  }
  .brand-square {
    width: 16px;
    height: 16px;
    background: var(--brand-green);
  }
  .brand-name {
    font-weight: 700;
    font-size: 40px;
    color: var(--brand-blue);
    letter-spacing: 0.5px;
  }
  .card-back {
    background: var(--brand-blue);
    color: var(--text-white);
  }
  .corner-frame {
    position: absolute;
    top: 22px;
    right: 24px;
    width: 46%;
    height: 58%;
    border-top: 1px solid var(--brand-green);
    border-right: 1px solid var(--brand-green);
  }
  .person {
    position: absolute;
    left: 40px;
    top: 104px;
  }
  .person-name {
    font-size: 15px;
    font-weight: 500;
  }
  .person-title {
    font-size: 11px;
    color: var(--brand-green);
    margin-left: 4px;
  }
  .person-line {
    font-size: 11px;
    line-height: 16px;
  }
  .person-contact { margin-top: 8px; }
  .office {
    position: absolute;
    left: 40px;
    bottom: 34px;
    font-size: 11px;
    line-height: 16px;
  }
  .office-web { color: var(--brand-green); }
</style>
</head>
<body>
  <main class="canvas">
    <section class="card card-front" aria-label="Business card front">
      <div class="brand-lockup">
        <span class="brand-square"></span>
        <span class="brand-name">QLTV Realty</span>
      </div>
    </section>

    <section class="card card-back" aria-label="Business card back">
      <div class="corner-frame"></div>
      <div class="person">
        <p><span class="person-name">Dev Kulkarni</span><span class="person-title">Managing Broker</span></p>
        <div class="person-contact">
          <p class="person-line">312-948-6051</p>
          <p class="person-line">dev.kulkarni@qltvrealty.com</p>
        </div>
      </div>
      <div class="office">
        <p>5197 Larchmere Ave., Skokie, IL 60093-1725</p>
        <p>312-682-9307</p>
        <p class="office-web">www.qltvrealty.com</p>
      </div>
    </section>
  </main>
</body>
</html>
```